GRAPHIC DESIGN FOR RESTAURANT MENU FOR HEALTHY RESTAURANT

I am looking for a graphic design for our menu displayed on a TV screen. Please ensure the file will fit on a TV screen nicely. We are looking for a clean design , with the following items. We would also like to include a couple of photos.
Breakfast:
Protein Chocolate Chip Pancakes - $12.95
Sunny Trail Burrito- $11.95
Tall Barn Omelette - $12.95
Lunch
Butter Chicken - $13.95
Chicken Quesadilla - $13.45
Coconut Garlic Shrimp - $15.95
Goat Cheese Stuffed Chicken - $14.95
Chipotle Steak Wrap - $12.95
Turkey Meatball Fettuccini - $13.45
Chicken Alfredo - $13.45
Chicken Parmesan - $13.95
Pesto Chicken Pasta - $13.45
Steak Bite and Green Stir Fry - $13.45
Asian Chicken Teriyaki - $13.45
Please include our logo
Restaurant

```html
<!DOCTYPE html>
<html lang="en">
<head>
<meta charset="utf-8">
<title>Greenfork Menu Board</title>
<link href="https://fonts.googleapis.com/css2?family=Alfa+Slab+One&family=Roboto:wght@700&display=swap" rel="stylesheet">
<style>
  :root {
    --page-bg: #f4f4f4;
    --board-bg: #111111;
    --heading-green: #1fa81f;
    --item-yellow: #f0bf0f;
    --price-orange: #e0741c;
    --brand-grey: #8a8a8a;
    --photo-light: #e4e7ea;
    --photo-mid: #c9ced3;
  }
  * { margin: 0; padding: 0; box-sizing: border-box; }
  html, body {
    width: 1200px; height: 800px; overflow: hidden;
    background: var(--page-bg);
  }
  .menu-board {
    position: absolute; left: 0; top: 62px;
    width: 1200px; height: 675px;
    background: var(--board-bg);
    font-family: "Alfa Slab One", Georgia, serif;
  }
  .menu-column {
    position: absolute; left: 56px; top: 70px; width: 650px;
  }
  .section-title {
    color: var(--heading-green);
    font-size: 30px; letter-spacing: 2px;
    margin-bottom: 24px;
  }
  .section-lunch { margin-top: 86px; }
  .item-list { list-style: none; }
  .menu-item {
    display: flex; align-items: baseline;
    height: 27px;
    color: var(--item-yellow);
    font-size: 19px; letter-spacing: 1px;
    text-transform: uppercase;
  }
  .item-leader {
    flex: 1; margin: 0 10px;
    border-bottom: 2px dashed var(--item-yellow);
    transform: translateY(-5px);
  }
  .item-price {
    width: 84px; text-align: right;
    color: var(--price-orange);
    font-family: "Roboto", Arial, sans-serif; font-weight: 700;
    font-size: 19px; letter-spacing: 0.5px;
  }
  .photo-grid {
    position: absolute; left: 760px; top: 130px;
    width: 400px;
  }
  .photo-row { display: flex; gap: 14px; }
  .food-photo {
    width: 193px; height: 190px;
    background: radial-gradient(circle at 50% 55%, #f2efe8 0%, var(--photo-light) 45%, var(--photo-mid) 100%);
  }
  .brand-block {
    height: 150px;
    display: flex; align-items: center; justify-content: center; gap: 14px;
  }
  .brand-dot {
    width: 22px; height: 22px; border-radius: 50%;
    background: var(--heading-green);
  }
  .brand-name {
    color: var(--brand-grey);
    font-size: 46px; letter-spacing: 3px;
  }
</style>
</head>
<body>
  <main class="menu-board">
    <section class="menu-column">
      <h2 class="section-title">BREAKFAST</h2>
      <ul class="item-list">
        <li class="menu-item"><span class="item-name">Protein Chocolate Chip Pancakes</span><span class="item-leader"></span><span class="item-price">$12.95</span></li>
        <li class="menu-item"><span class="item-name">Sunny Trail Burrito</span><span class="item-leader"></span><span class="item-price">$11.95</span></li>
        <li class="menu-item"><span class="item-name">Tall Barn Omelette</span><span class="item-leader"></span><span class="item-price">$12.95</span></li>
      </ul>

      <h2 class="section-title section-lunch">LUNCH</h2>
      <ul class="item-list">
        <li class="menu-item"><span class="item-name">Butter Chicken</span><span class="item-leader"></span><span class="item-price">$13.95</span></li>
        <li class="menu-item"><span class="item-name">Chicken Quesadilla</span><span class="item-leader"></span><span class="item-price">$13.45</span></li>
        <li class="menu-item"><span class="item-name">Coconut Garlic Shrimp</span><span class="item-leader"></span><span class="item-price">$15.95</span></li>
        <li class="menu-item"><span class="item-name">Goat Cheese Stuffed Chicken</span><span class="item-leader"></span><span class="item-price">$14.95</span></li>
        <li class="menu-item"><span class="item-name">Chipotle Steak Wrap</span><span class="item-leader"></span><span class="item-price">$12.95</span></li>
        <li class="menu-item"><span class="item-name">Turkey Meatball Fettuccini</span><span class="item-leader"></span><span class="item-price">$13.45</span></li>
        <li class="menu-item"><span class="item-name">Chicken Alfredo</span><span class="item-leader"></span><span class="item-price">$13.45</span></li>
        <li class="menu-item"><span class="item-name">Chicken Parmesan</span><span class="item-leader"></span><span class="item-price">$13.95</span></li>
        <li class="menu-item"><span class="item-name">Pesto Chicken Pasta</span><span class="item-leader"></span><span class="item-price">$13.45</span></li>
        <li class="menu-item"><span class="item-name">Steak Bite and Green Stir Fry</span><span class="item-leader"></span><span class="item-price">$13.45</span></li>
        <li class="menu-item"><span class="item-name">Asian Chicken Teriyaki</span><span class="item-leader"></span><span class="item-price">$13.45</span></li>
      </ul>
    </section>

    <aside class="photo-grid">
      <div class="photo-row">
        <div class="food-photo" role="img" aria-label="Omelette with toast on a white plate on a pale wooden table"></div>
        <div class="food-photo" role="img" aria-label="Stack of chocolate chip pancakes on a white plate on a pale wooden table"></div>
      </div>
      <div class="brand-block">
        <span class="brand-dot"></span>
        <span class="brand-name">GREENFORK</span>
      </div>
      <div class="photo-row">
        <div class="food-photo" role="img" aria-label="Halved steak wraps on paper on a pale wooden table"></div>
        <div class="food-photo" role="img" aria-label="Bowl of chicken pasta in tomato sauce on a pale wooden table"></div>
      </div>
    </aside>
  </main>
</body>
</html>
```